Personal coach needs brochure design for inspirational essay about authenticity

Overview:
I want a beautiful brochure, 11”x17” that folds to 8-1/2”x11” with 4 pages. Think of it as an oversize greeting card.
• Front cover: photograph of a dancer and title with attribution of quote (Lumafold jpeg photo attached)
• Inside spread: Copy (Helena Brisk copy attached) with some appropriate illustration, based on cover photo
• Back cover: contact information, brief descriptive copy, two small photos (jpeg photo attached; see copy for direction)
Copy for front cover title, inside spread and back cover is attached in doc titled "Helena Brisk copy"

Purpose of brochure:
I'm a personal coach and once a year I produce a 4-page illustrated inspirational essay, which invites personal reflection on living a more mindful, meaningful life. Most people I send them to collect them. Someday in the future I'd like to put a collection of these essays into a coffee table book and also create a website for the collection, which is related to the personal coaching that I do.
I have the brochures printed hard copy. I have attached a few examples from previous years. Each has a unique design related to its theme.

Concept:
This year’s essay theme, “There will only ever be one you!” is based on a quote by Helena Brisk, a famous modern dancer. The complete quote, which appears in the copy, is about being true to one’s authentic self. The essay is not about dance, but because the author of the quote was a dancer who personified this theme of being unique to self, I have selected a photo of dance for the cover.

Design Guidance:
Front cover: One possibility is to expand the background color of the Lumafold photo so the photo seems to emerge from the background. But I am open to ideas. I think the photo is artsy enough as it is, but there may be other ways to treat it (e.g. special effects) that would also work. The title should appear somewhere. Make the attribution (--Helena Brisk) in smaller type than the title.

Inside Spread: There may be ways to borrow a design motif from the cover photo to make the inside spread more visually interesting, i.e., not just straight copy. I think it may be helpful to make the font size of the quote larger than the rest of the copy, but it has to be read in sequence. Or maybe it's printed in same size as copy, but then also repeated and displayed by itself in larger type.

Back cover: If you look at some of the other examples I’ve sent, you’ll see how the back cover is typically handled. I want a reduced version of the cover to be placed near the line that says "this is the 16th in a series.." Then, there’s a jpeg photo of Helena Brisk that should be placed next to the copy description of her.

Need extra days to review

```html
<!DOCTYPE html>
<html lang="en">
<head>
<meta charset="utf-8">
<title>There will only ever be one you! — Brochure</title>
<link href="https://fonts.googleapis.com/css2?family=Raleway:wght@400;500;600&family=Gochi+Hand&display=swap" rel="stylesheet">
<style>
  :root {
    --backdrop: #d4d4d4;
    --paper: #efefef;
    --paper-white: #f6f6f6;
    --orange: #dd6512;
    --orange-light: #e8842e;
    --grey-shape: #cdcdcd;
    --ring: #dcdcdc;
    --ink: #3a3a3a;
    --ink-soft: #5a5a5a;
    --dancer-dark: #1f242c;
    --dancer-mid: #4a5566;
  }
  * { box-sizing: border-box; margin: 0; padding: 0; }
  html, body { width: 1200px; height: 859px; overflow: hidden; }
  body { background: var(--backdrop); font-family: "Raleway", sans-serif; color: var(--ink); position: relative; }

  .page { position: absolute; top: 196px; width: 360px; height: 466px; background: var(--paper); overflow: hidden; box-shadow: 0 6px 18px rgba(0,0,0,.12); }
  .page > svg { position: absolute; inset: 0; }
  .spread-left { left: 40px; }
  .spread-right { left: 400px; background: var(--paper-white); }
  .front-cover { left: 800px; }

  .body-copy { position: absolute; font-size: 6.2px; line-height: 1.6; text-align: justify; color: var(--ink-soft); }
  .body-copy p + p { margin-top: 5px; }
  .rule { position: absolute; height: 1.5px; background: var(--orange); }

  .left-copy { left: 30px; top: 284px; width: 300px; }
  .left-rule { left: 30px; top: 276px; width: 62px; }

  .intro-copy { left: 40px; top: 92px; width: 290px; }
  .quote-mark { position: absolute; left: 22px; top: 150px; font-size: 38px; font-weight: 600; color: var(--orange); line-height: 1; }
  .pull-quote { position: absolute; left: 52px; top: 168px; width: 282px; font-size: 10.4px; line-height: 1.42; color: var(--ink); font-weight: 500; }
  .closing-copy { left: 40px; top: 330px; width: 290px; }

  .cover-title { position: absolute; left: 92px; top: 360px; width: 250px; font-family: "Gochi Hand", cursive; color: #fff; font-size: 31px; line-height: 1.12; text-align: center; }
  .cover-attribution { position: absolute; left: 92px; top: 436px; width: 250px; font-family: "Gochi Hand", cursive; color: #fff; font-size: 12px; text-align: center; }
</style>
</head>
<body>

  <!-- Inside spread, left page -->
  <section class="page spread-left">
    <svg width="360" height="466" viewBox="0 0 360 466">
      <defs>
        <linearGradient id="orangeSweepL" x1="0" y1="1" x2="1" y2="0">
          <stop offset="0" stop-color="#d25c0c"/>
          <stop offset="1" stop-color="#e8842e"/>
        </linearGradient>
        <linearGradient id="dancerTone" x1="0" y1="0" x2="0" y2="1">
          <stop offset="0" stop-color="#2a1a14"/>
          <stop offset=".5" stop-color="#1f242c"/>
          <stop offset="1" stop-color="#4a5566"/>
        </linearGradient>
      </defs>
      <path d="M0 0 H360 V66 C260 110 150 180 0 236 Z" fill="url(#orangeSweepL)"/>
      <path d="M0 256 C80 240 160 226 222 218 C246 214 252 232 234 242 L64 330 L0 330 Z" fill="var(--grey-shape)"/>
      <path d="M168 44 C190 40 206 70 222 96 C248 106 262 140 258 170 C250 200 230 220 214 238 C208 256 206 274 196 284 C190 270 192 254 186 236 C176 206 168 170 166 140 C158 110 160 70 168 44 Z" fill="url(#dancerTone)" role="img" aria-label="Photograph of a leaping dancer in a flowing dark dress"/>
    </svg>
    <div class="rule left-rule"></div>
    <div class="body-copy left-copy">
      <p>In the rural Ohio village where I grew up, one of the highlights of Sunday morning church service — in between congregational hymn-singing and the preacher's sermon — was the "special selection," a musical performance by a parishioner. Typically, it was a vocalist or instrumental on piano, organ or violin. One Sunday, we were surprised by an unusual performance. A plump, buxom farm wife approached the pulpit, puckered up her lips and unexpectedly began to whistle the hymn "Lantern on the Hill." As a 10-year-old, I found this hilarious as I tried to choke back my wide-eyed amazement and giggles.</p>
      <p>Despite the irreverence of my pre-adolescent reaction, this memory has stayed with me for decades as an iconic example of the wonderment of individual differences. Of the delight I find in witnessing someone express herself in sometimes surprising and even courageous ways. Of the marvel of beholding a person be truly authentic and uniquely original.</p>
      <p>Someone who personified the irrepressible impulse to express her individuality was the early 20th century dancer and choreographer Helena Brisk. A pioneer of modern dance, she threw tradition overboard and was inspired to dance in a way that was a radical departure from the formalized style and rigidly dictated forms of classical ballet. Brisk felt compelled to express the rawness and emotion of human experience in her dancing — not just present a form of pretty entertainment. Iconoclastically brilliant, she created a new language of dance, a revolutionary vocabulary of movement that electrified the stage, often</p>
    </div>
  </section>

  <!-- Inside spread, right page -->
  <section class="page spread-right">
    <svg width="360" height="466" viewBox="0 0 360 466">
      <defs>
        <linearGradient id="orangeSweepR" x1="0" y1="0" x2="1" y2="0">
          <stop offset="0" stop-color="#e07524"/>
          <stop offset=".35" stop-color="#eca266"/>
          <stop offset="1" stop-color="#e07524"/>
        </linearGradient>
      </defs>
      <path d="M0 0 H360 V16 C250 20 120 40 0 112 Z" fill="url(#orangeSweepR)"/>
      <path d="M360 36 V86 L268 90 C256 90 256 80 266 74 Z" fill="var(--grey-shape)"/>
    </svg>
    <div class="body-copy intro-copy">
      <p>creating a visceral response in the audience. In her biography of Brisk, her friend and equally talented choreographer Clara Vance recalled that despite sensational reviews for her own innovative work in the Broadway musical <em>Prairie Song</em>, Vance had a gnawing feeling that her work was only mediocre. Vance confessed her anxieties to Brisk who listened quietly and then responded, "There will only ever be one you!" Continuing, she added:</p>
    </div>
    <div class="quote-mark">&ldquo;</div>
    <blockquote class="pull-quote">"There is a vitality, a life-force, an energy, a quickening that is translated through you into action. And because there is only one of you in all of time, this expression is unique. And if you block it, the world will not have it. It is not your business to determine how good it is nor how valuable nor how it compares with other expressions. It is your business to keep it yours clearly and directly, to keep the channel open. You have to keep open and aware directly to the urges that motivate you. Above all else, keep the channel open!"</blockquote>
    <div class="body-copy closing-copy">
      <p>Brisk's wisdom reminds us that we must not hold back or judge our gifts in moments when we doubt ourselves or when we worry that we're not good enough. She asks us to be fearless and to "keep the channel open."</p>
      <p>Guard the precious miracle of your own uniqueness. Find that home where you feel you are your most authentic self. There will only ever be one of you, and our world would be a drab, boring place without the differences of others. Our world is richer for every voice that dares to sing its own song, and for every step taken in a rhythm all its own.</p>
    </div>
  </section>

  <!-- Front cover -->
  <section class="page front-cover">
    <svg width="360" height="466" viewBox="0 0 360 466">
      <defs>
        <linearGradient id="dancerToneCover" x1="0" y1="0" x2="0" y2="1">
          <stop offset="0" stop-color="#2a1a14"/>
          <stop offset=".45" stop-color="#1f242c"/>
          <stop offset="1" stop-color="#4a5566"/>
        </linearGradient>
      </defs>
      <path d="M0 0 H118 C138 4 150 26 144 50 C138 70 118 84 108 100 C92 126 92 180 92 260 V466 H0 Z" fill="var(--orange)"/>
      <circle cx="240" cy="196" r="128" fill="none" stroke="var(--ring)" stroke-width="7"/>
      <circle cx="240" cy="196" r="112" fill="#e3e3e3"/>
      <path d="M170 84 C190 70 270 66 310 96 C346 126 350 200 336 240 C326 270 300 282 284 270 C256 250 240 210 212 170 C190 140 160 116 170 84 Z" fill="var(--orange)"/>
      <path d="M0 466 V330 C40 330 130 330 190 330 C240 330 262 318 286 312 C304 308 314 320 324 340 L360 410 V466 Z" fill="var(--orange-light)"/>
      <path d="M236 70 C254 62 270 96 292 112 C318 122 336 152 330 188 C322 224 296 250 268 262 C242 276 204 296 178 318 C172 332 168 346 158 352 C152 336 164 316 178 298 C196 270 206 236 208 204 C212 160 226 110 236 70 Z" fill="url(#dancerToneCover)" role="img" aria-label="Photograph of a leaping dancer in a flowing dark dress, arms raised"/>
    </svg>
    <h1 class="cover-title">There will only ever be one you!</h1>
    <p class="cover-attribution">-Helena Brisk-</p>
  </section>

</body>
</html>
```